KLT Proposal Flyer Document

Hi Marketing Team, Require this MS Word doc in a professional proposal flyer format that I can use for proposal to customers, it needs to reflect the KLT Business and Culture, which is a HR Consultancy firm so lots pics of people welcoming, reading at meetings ect, so its people and business focused. Pls note the document needs to be able to be interacted with as well as saved and emailed to clients in PDF format, so pls keep this in mind when doing the design. Thanks very much

Target Market(s)

HR Managers, Global Business Leaders and Decision Makers

Colors
ec1f27

Requirements
Must have
• Professional look

```html
<!DOCTYPE html>
<html lang="en">
<head>
<meta charset="utf-8">
<title>KLT Proposal Flyer Document</title>
<link rel="stylesheet" href="https://fonts.googleapis.com/css2?family=Montserrat:wght@400;500;600;700;800&display=swap">
<style>
:root{
  --red:#ec1f27;
  --ink:#222;
  --dark:#2b2b2b;
  --paper:#f1f1f1;
  --paper-hi:#fafafa;
  --backdrop:#a9a9a9;
  --rule:#c9c9c9;
}
*{box-sizing:border-box;margin:0;padding:0}
html,body{width:1200px;height:2741px;overflow:hidden}
body{background:var(--backdrop);font-family:"Montserrat",sans-serif;color:var(--ink)}
.stage{position:absolute;left:0;top:0;width:1128px;height:2576px;transform:scale(1.0638);transform-origin:0 0}
.page{position:absolute;width:490px;height:693px;background:linear-gradient(180deg,var(--paper-hi),var(--paper));box-shadow:0 4px 10px rgba(0,0,0,.35);overflow:hidden;transform-origin:0 0}
.page--cover{left:307px;top:168px;transform:scale(1.082)}
.page--scope{left:57px;top:1104px}
.page--plan{left:573px;top:1104px}
.page--questions{left:319px;top:1824px}

.masthead{height:100px;display:flex;flex-direction:column;align-items:center;justify-content:center;background:linear-gradient(180deg,#f7f7f7,#ececec)}
.brand{display:flex;align-items:center;gap:8px;color:var(--red);font-weight:800}
.brand-dot{width:48px;height:48px;border-radius:50%;background:var(--red)}
.brand-name{font-size:62px;line-height:.9;letter-spacing:1px}
.brand-sub{color:var(--red);font-weight:800;font-size:14.5px;letter-spacing:.3px;margin-top:2px}
.tagline{height:26px;background:var(--red);color:#fff;font-size:12.5px;text-align:center;line-height:26px;font-weight:500}

.footer{position:absolute;left:0;bottom:0;width:100%;height:37px;background:var(--red);display:flex;align-items:center}
.footer-phone{height:100%;width:158px;background:#111;color:#fff;display:flex;align-items:center;gap:8px;padding-left:16px;font-weight:700;font-size:14px;clip-path:polygon(0 0,100% 0,94% 100%,0 100%)}
.footer-links{flex:1;color:#fff;font-size:7.6px;display:flex;align-items:center;gap:8px;padding-left:8px}
.page-num{width:18px;height:18px;border-radius:50%;background:#fff;color:#111;font-weight:700;font-size:9px;display:flex;align-items:center;justify-content:center;margin-left:auto;margin-right:14px}

.photo{height:183px;background:linear-gradient(135deg,#d9d6d2,#8c8a8c 45%,#c7c3bf)}
.values{height:194px;background:var(--dark);position:relative}
.values-line{position:absolute;left:97px;right:94px;top:48px;height:2px;background:#fff}
.value{position:absolute;top:14px;width:140px;text-align:center;color:#fff}
.value-ring{width:72px;height:72px;border-radius:50%;background:#fff;margin:0 auto;display:flex;align-items:center;justify-content:center}
.value-core{width:62px;height:62px;border-radius:50%;background:var(--red);border:2px solid #fff;box-shadow:0 0 0 2px var(--red);display:flex;align-items:center;justify-content:center}
.value h3{color:var(--red);font-size:9.5px;font-weight:700;margin:12px 0 6px}
.value p{font-size:7.5px;line-height:1.3}

.section-title{color:var(--red);font-weight:800;font-size:15px}
.ticks{list-style:none}
.ticks li{position:relative;padding-left:14px;font-size:8.6px;line-height:1.3}
.ticks li::before{content:"";position:absolute;left:0;top:1px;width:8px;height:8px;border:1px solid var(--red);border-radius:50%}
.ticks li::after{content:"";position:absolute;left:3px;top:2.5px;width:2px;height:4px;border:solid var(--red);border-width:0 1.2px 1.2px 0;transform:rotate(40deg)}
.offerings{padding:10px 22px 0}
.offerings .ticks li{margin-top:10px}

.scope-band{height:102px;background:var(--dark);padding:16px 22px;color:#fff}
.scope-band p{font-size:8.4px;line-height:1.3;margin-top:6px}
.scope-body{padding:22px 22px 0}
.lead{color:var(--red);font-weight:700;font-size:11px;line-height:1.3}
.scope-body .ticks{margin-top:12px}
.scope-body .ticks li{margin-bottom:9px}
.lifecycle{position:absolute;left:22px;top:454px;width:305px;height:184px;background:radial-gradient(circle at 62% 52%,#f4c66d 0,#7fc3c0 32%,#e9e9e9 50%,#fff 70%);border:1px solid #ddd}
.reference{position:absolute;left:333px;top:454px;width:135px;height:184px;background:var(--red);color:#fff;font-weight:700;font-size:10.5px;line-height:1.25;text-align:center;display:flex;align-items:center;justify-content:center;padding:10px}

.plan-band{height:182px;background:var(--dark);padding:10px 18px 0}
.grid{width:100%;border-collapse:collapse;table-layout:fixed}
.grid th{background:#1b1b1b;color:#fff;font-size:7.4px;font-weight:700;height:24px}
.grid td{height:22px;border:1px solid var(--rule);font-size:8px;font-weight:700;padding:0 6px}
.plan-band .grid{margin-top:8px;border:2px solid #fff}
.plan-band .grid th{background:#fff;color:#111;border:1px solid #2b2b2b}
.plan-band .grid td{background:#111;border:1px solid #fff}
.plan-block{padding:12px 18px 0}
.plan-block .grid{margin-top:8px;border:2px solid #1b1b1b}
.plan-block .grid td{background:#fff}
.plan-block .grid th{border:1px solid #444}
.sub{text-align:left}

.questions{padding:14px 24px 0}
.questions .section-title{font-size:11px;line-height:1.25}
.questions .ticks{margin-top:4px}
.questions .ticks li{font-size:7.5px;line-height:1.22;padding-left:12px}
.questions .ticks li::before{width:7px;height:7px}
.questions .ticks li::after{left:2.6px;top:2px;height:3.5px}
.questions h4{color:var(--red);font-weight:700;font-size:11px;margin-top:20px}
.questions h2{color:var(--red);font-weight:800;font-size:14px;margin-top:14px}
.questions p{font-size:7.6px;line-height:1.3;margin-top:4px}
.questions hr{border:0;border-top:1px solid #999;margin-top:12px}
</style>
</head>
<body>
<div class="stage">

<!-- Page 1 -->
<section class="page page--cover">
  <header class="masthead">
    <div class="brand"><span class="brand-dot"></span><span class="brand-name">KLT</span></div>
    <div class="brand-sub">KELTON TALENT CONSULTING</div>
  </header>
  <div class="tagline">HR Strategy | HR Operations | HR Projects | Business Solutions.</div>
  <div class="photo" role="img" aria-label="Photo of a business team meeting around a conference table with a whiteboard"></div>
  <div class="values">
    <div class="values-line"></div>
    <div class="value" style="left:27px">
      <div class="value-ring"><div class="value-core">
        <svg width="30" height="30" viewBox="0 0 24 24"><polygon points="12,2 14.9,8.6 22,9.2 16.6,14 18.2,21 12,17.3 5.8,21 7.4,14 2,9.2 9.1,8.6" fill="#fff"/></svg>
      </div></div>
      <h3>OUR VISION</h3>
      <p>Build high performing<br>HR Capital Talent and Solutions for local and global business leaders for current and future business needs.</p>
    </div>
    <div class="value" style="left:176px">
      <div class="value-ring"><div class="value-core">
        <svg width="32" height="32" viewBox="0 0 24 24" fill="none" stroke="#fff" stroke-width="1.6"><circle cx="12" cy="12" r="9"/><circle cx="12" cy="12" r="5.5"/><circle cx="12" cy="12" r="2"/><path d="M12 12 L20 4"/></svg>
      </div></div>
      <h3>OUR PURPOSE</h3>
      <p>Our Purpose is to provide HR Strategy, Hands on HR Operational Services and deliver timely Projects to develop, nurture talent and find the best solutions for global business leaders.</p>
    </div>
    <div class="value" style="left:326px">
      <div class="value-ring"><div class="value-core">
        <svg width="32" height="32" viewBox="0 0 24 24"><circle cx="12" cy="12" r="9" fill="none" stroke="#fff" stroke-width="1.6"/><polygon points="12,3 13.5,10.5 21,12 13.5,13.5 12,21 10.5,13.5 3,12 10.5,10.5" fill="#fff"/></svg>
      </div></div>
      <h3>OUR STRATEGY</h3>
      <p>To differentiate ourselves based on having a positive impact and providing an exceptional client care experience.</p>
    </div>
  </div>
  <div class="offerings">
    <h2 class="section-title">SERVICE OFFERINGS</h2>
    <ul class="ticks">
      <li>Consult with Senior Leaders on critical business issues and find the best solutions.</li>
      <li>Work with the business to Build Strategies across, Employee Branding # Employee Engagement # Performance Management # Talent Management # Best Practices to accelerate business growth.</li>
      <li>Recommend solutions and tools to add structure to the Human Resources function to create employee engagement, positive communications and enable businesses to scale.</li>
      <li>Support business leaders in HR Projects aligned to business improvement and growth.</li>
    </ul>
  </div>
  <footer class="footer">
    <div class="footer-phone"><svg width="16" height="16" viewBox="0 0 24 24" fill="none" stroke="#fff" stroke-width="1.6"><circle cx="12" cy="12" r="10.5"/><path d="M8.5 6.5l2 2.5-1.2 1.5c.8 1.7 2.1 3 3.8 3.8l1.5-1.2 2.5 2-1.3 1.8c-4.2-.3-8.6-4.7-8.9-8.9z" fill="#fff" stroke="none"/></svg>+ 65 9000 4172</div>
    <div class="footer-links"><span>✉ hello@keltontalent.com</span><span>◎ www.keltontalent.org</span><span class="page-num">1</span></div>
  </footer>
</section>

<!-- Page 2 -->
<section class="page page--scope">
  <header class="masthead">
    <div class="brand"><span class="brand-dot"></span><span class="brand-name">KLT</span></div>
    <div class="brand-sub">KELTON TALENT CONSULTING</div>
  </header>
  <div class="tagline">HR Strategy | HR Operations | HR Projects | Business Solutions.</div>
  <div class="scope-band">
    <h2 class="section-title">1. PROJECT SCOPE</h2>
    <p>Initial communication to understand current HR Framework in place or leverage from Regional/ Global Head Office. Understanding the current HR Model in place and Assessment of current HR Practices across the HR Employee Lifecycle and key business strategies and goals currently in place.</p>
  </div>
  <div class="scope-body">
    <p class="lead">The main areas of focus is an initial conversation regards to understanding of the current HR Landscape, current Model in Place, current practices, systems and policies across the organization.</p>
    <ul class="ticks">
      <li>Review and understand current HR Practices, culture, values and work environment. Style of business structure and leadership in place currently.</li>
      <li>Current HR Model in place, current systems, practices across the Employee Lifecycle as aligned to Principles of Fair Employment Practices, FWPA Guidelines and The Open Workplace Model as a reference model.</li>
      <li>Key Business Goals, Strategy, Plans and Priorities current and the future.</li>
      <li>Gain an understanding of current Employee Pulse and any Recent Surveys</li>
      <li>Gain an understanding of current Safety Strategy that is in place with Covid-19, review policies to date.</li>
    </ul>
  </div>
  <div class="lifecycle" role="img" aria-label="Employee lifecycle wheel infographic from the Open Workplace model"></div>
  <div class="reference">“Hire, Inspire, Retire” Approach Reference: Adopted from the Open Workplace Employee LifeCycle Model, Author: Dana Morrow.</div>
  <footer class="footer">
    <div class="footer-phone"><svg width="16" height="16" viewBox="0 0 24 24" fill="none" stroke="#fff" stroke-width="1.6"><circle cx="12" cy="12" r="10.5"/><path d="M8.5 6.5l2 2.5-1.2 1.5c.8 1.7 2.1 3 3.8 3.8l1.5-1.2 2.5 2-1.3 1.8c-4.2-.3-8.6-4.7-8.9-8.9z" fill="#fff" stroke="none"/></svg>+ 65 9000 4172</div>
    <div class="footer-links"><span>✉ hello@keltontalent.com</span><span>◎ www.keltontalent.org</span><span class="page-num">2</span></div>
  </footer>
</section>

<!-- Page 3 -->
<section class="page page--plan">
  <header class="masthead">
    <div class="brand"><span class="brand-dot"></span><span class="brand-name">KLT</span></div>
    <div class="brand-sub">KELTON TALENT CONSULTING</div>
  </header>
  <div class="tagline">HR Strategy | HR Operations | HR Projects | Business Solutions.</div>
  <div class="plan-band">
    <h2 class="section-title">2. PROJECT RESOURCES</h2>
    <table class="grid">
      <colgroup><col style="width:25%"><col style="width:37%"><col style="width:38%"></colgroup>
      <tr><th>RESOURCES</th><th>VALUE ADD POSITION</th><th>YEARS OF EXPERIENCE</th></tr>
      <tr><td></td><td></td><td></td></tr>
      <tr><td></td><td></td><td></td></tr>
      <tr><td></td><td></td><td></td></tr>
      <tr><td></td><td></td><td></td></tr>
      <tr><td></td><td></td><td></td></tr>
    </table>
  </div>
  <div class="plan-block">
    <h2 class="section-title">3. PROJECT BUDGET</h2>
    <table class="grid">
      <colgroup><col style="width:50%"><col style="width:12%"><col style="width:13%"><col style="width:12%"><col style="width:13%"></colgroup>
      <tr><th class="sub" style="padding-left:24px">PROJECT BUDGET</th><th colspan="2">FORECAST COST</th><th colspan="2">REAL COST</th></tr>
      <tr><td></td><td>$</td><td>TIME</td><td>$</td><td>TIME</td></tr>
      <tr><td></td><td></td><td></td><td></td><td></td></tr>
      <tr><td></td><td></td><td></td><td></td><td></td></tr>
      <tr><td></td><td></td><td></td><td></td><td></td></tr>
      <tr><td></td><td></td><td></td><td></td><td></td></tr>
    </table>
  </div>
  <div class="plan-block">
    <h2 class="section-title">4.PROJECT MILESTONES MAJOR TASKS</h2>
    <table class="grid">
      <colgroup><col style="width:18%"><col style="width:18%"><col style="width:13%"><col style="width:14%"><col style="width:19%"><col style="width:18%"></colgroup>
      <tr><th>TASK NAME</th><th>ASSIGNED TO</th><th>START DATE</th><th>END DATE</th><th>DURATION in days</th><th>STATUS</th></tr>
      <tr><td style="height:46px">PROJECT ASSESSMENT.</td><td></td><td></td><td></td><td></td><td></td></tr>
    </table>
  </div>
  <footer class="footer">
    <div class="footer-phone"><svg width="16" height="16" viewBox="0 0 24 24" fill="none" stroke="#fff" stroke-width="1.6"><circle cx="12" cy="12" r="10.5"/><path d="M8.5 6.5l2 2.5-1.2 1.5c.8 1.7 2.1 3 3.8 3.8l1.5-1.2 2.5 2-1.3 1.8c-4.2-.3-8.6-4.7-8.9-8.9z" fill="#fff" stroke="none"/></svg>+ 65 9000 4172</div>
    <div class="footer-links"><span>✉ hello@keltontalent.com</span><span>◎ www.keltontalent.org</span><span class="page-num">3</span></div>
  </footer>
</section>

<!-- Page 4 -->
<section class="page page--questions">
  <header class="masthead">
    <div class="brand"><span class="brand-dot"></span><span class="brand-name">KLT</span></div>
    <div class="brand-sub">KELTON TALENT CONSULTING</div>
  </header>
  <div class="tagline">HR Strategy | HR Operations | HR Projects | Business Solutions.</div>
  <div class="questions">
    <h2 class="section-title">Initial Conversation, Collaboration with HR Leadership Team and Senior Management.</h2>
    <ul class="ticks">
      <li>Assessment of current HR Employee Lifecycle and current business goals in place</li>
      <li>HR Health Check in terms of current strategies in place, practices, processes and systems in place.</li>
      <li>How does the website look for attracting new employees ?</li>
      <li>Are there clear job specifications in place ?</li>
      <li>How developed is the Employee Handbook ?</li>
      <li>Current framework and policies in place ?</li>
      <li>Is there an employee referral program in place ?</li>
      <li>What is the level of sophistication across the HR Strategy ?</li>
      <li>What are the business key goals ?</li>
      <li>What are the business key priorities ?</li>
      <li>Which technology is in place for recruiting ?</li>
      <li>Is there Regular and Ongoing Performance Management ?</li>
      <li>Which technology is in place for learning and development ?</li>
      <li>What sort of engagement strategies are currently in place for employees ?</li>
      <li>Have any recent ‘ Employee Pulse surveys been conducted ?</li>
      <li>What was the result of the last ‘ Employee Survey ‘ in terms of NPS – Net Promoter Score, How satisfied where employees with working at the company ?</li>
      <li>What would management and the leadership team like help with ?</li>
    </ul>
    <h4>Human Resources, Leadership Team, Senior Management Perspective ?</h4>
    <ul class="ticks"><li>Feedback and open dialogue to the above questions.</li></ul>
    <h2>5.COMMUNICATION PLAN</h2>
    <p>Per weekly Team meetings each Friday on Huddle with Team Members for full Team Engagement to keep communications positive and open for WFH, remote workers and those back in the office.</p>
    <hr>
    <h2>6. OTHER TEAM MEMBER IDEAS.</h2>
    <hr>
    <h2>7. EMPHASIS ON QUALITY AND BEST PRACTICES.</h2>
    <hr>
    <h2>8. HR ANALYTICS AND INSIGHTS.</h2>
    <p>Sample HR Metrics that are data driven and can be insightful for Business Performance and track performance, to gain insight and from this data build out Career Development Maps to help team members grow, build individual capabilities and competencies to drive engagement and accelerate business performance. Example : Performance Metrics</p>
  </div>
  <footer class="footer">
    <div class="footer-phone"><svg width="16" height="16" viewBox="0 0 24 24" fill="none" stroke="#fff" stroke-width="1.6"><circle cx="12" cy="12" r="10.5"/><path d="M8.5 6.5l2 2.5-1.2 1.5c.8 1.7 2.1 3 3.8 3.8l1.5-1.2 2.5 2-1.3 1.8c-4.2-.3-8.6-4.7-8.9-8.9z" fill="#fff" stroke="none"/></svg>+ 65 9000 4172</div>
    <div class="footer-links"><span>✉ hello@keltontalent.com</span><span>◎ www.keltontalent.org</span><span class="page-num">4</span></div>
  </footer>
</section>

</div>
</body>
</html>
```